PathVerdantia Community/ Talent Gallery

PathVerdantia is developing a collaborative career course, with coaching and community exchange. Goal is to offer a platform where talented candidates can show their expertise and find projects, partners, and develop their online portfolios!

Here is a good example of the type of thing we hope to create with focus on sustainability focused talent to task matching
http://www.halbrook-example.com/global-themes/employment-and-growth/connecting-talent-with-opportunity-in-the-digital-age

We hope to have a "grid style" gallery where it is easy to search by talent types and focus areas within the scope of "Sustainability" issues...Food/Water/Energy, Public Health, Technology, Sustainable Cities, Infrastructure, Education, Policy, Emerging Economies, Ecosystems, Social Innovation, inclusive Security, Equity Issues. For each topic/ header we hope to have candidates post their completed portfolios to exhibit resumes, biography, a case study... they may actually prepare these on other sites, but can link in OR alternately that they can easily create here, similar to "tellyou.biz" ....

Hope to include a blog space titled "Steering Through Seams", where people can mix it up across these topic issues as they are interdependent and often require partners across discipline areas! If possible another area where jobs related to these issues may be posted as project or job opportunities by potential employers.

If there is a way to create a feed from various job sites that already exist...like Jobrix...or http://www.greenventurehub-example.com/ that would be super great. Again...sort of a portal connection to bridge the gap ....instead of candidates having to search all the time, we are hoping they can advertise their talent and employers may search here for these well presented portfolios!

Target Market(s)

Educators, Students, Career Transitioners, Employers, Professional Associations, Talent Recruiters with focus on Sustainability related Talent to Task matching!

Industry/Entity Type

Sustainability

Number of Pages Required

4 page

Font styles to use
Sans Serif

Colors
3176b5
32b8a4
add136

Requirements
Must have
• Not sure about the coded/ uncoded option here....
• Must have - grid style area where Sustainability Professionals with varied focus areas can exhibit their talent portfolios
• appear as a Talent Gallery that starts with photos & obvious organization...other tabs to be in a menu.
• ability to search both talent and task opportunity areas to help coaches or community members make matches....some topic focused category or tag words to help make them searchable...???
• consistent professional styling to existing website and new artflock postcard shared in brief/ images area
• Interactive blog space where articles, issues may be posted, discussed
• Bulletin board or feed for project opportunities to be posted where candidates may locate them and/or employers may express specific "call" for talent..These may be Short term Internships, Projects, Consulting Team Opportunity, or Jobs/ part time to full time....
Nice to have
• A calendar area where we can post networking opportunities, issues presentations where potential partners can meet the next generation leaders, attend a forum or webinar presentation.
Should not have
• Too much text on front page...Should be clean design,

```html
<!DOCTYPE html>
<html lang="en">
<head>
<meta charset="utf-8">
<title>PathVerdantia – Talent Gallery</title>
<link href="https://fonts.googleapis.com/css2?family=Open+Sans:wght@400;600;700;800&display=swap" rel="stylesheet">
<style>
:root{
  --blue:#3176b5;
  --teal:#32b8a4;
  --lime:#add136;
  --navy:#1f3f63;
  --ink:#3a3f45;
  --muted:#8a9098;
  --line:#e3e6ea;
  --footer:#1c1e21;
  --white:#ffffff;
}
*{box-sizing:border-box;margin:0;padding:0}
html,body{width:1200px;height:2452px;overflow:hidden}
body{font-family:"Open Sans",Arial,sans-serif;color:var(--ink);background:var(--white);position:relative}

.hero{position:absolute;left:0;top:0;width:1200px;height:440px;overflow:hidden}
.hero-photo{position:absolute;inset:0;background:linear-gradient(115deg,#5d86ad 0%,#3f8fa6 40%,#3a7fb0 65%,#2f66a0 100%)}
.hero-band{position:absolute;left:0;top:290px;width:1200px;height:150px;background:linear-gradient(180deg,rgba(49,118,181,.55),rgba(49,118,181,.85))}
.brand{position:absolute;left:118px;top:28px;display:flex;align-items:center;gap:10px;color:var(--white);font-weight:700;font-size:22px}
.brand-dot{width:34px;height:34px;border-radius:50%;background:var(--teal)}
.menu-panel{position:absolute;right:24px;top:22px;width:270px;background:var(--white);padding:14px 0 10px}
.menu-label{position:absolute;right:30px;top:-16px;font-size:11px;font-weight:700;color:var(--white);letter-spacing:1px}
.menu-panel li{list-style:none;font-size:14px;color:var(--muted);padding:11px 26px 11px 60px;border-bottom:1px solid var(--line)}
.menu-panel li:first-child{color:var(--ink);font-weight:700}
.menu-panel li:last-child{border-bottom:none}
.hero-title{position:absolute;left:0;right:0;top:306px;text-align:center;color:var(--white);font-weight:800;font-size:23px;line-height:1.35;text-transform:uppercase}
.hero-sub{position:absolute;left:300px;right:300px;top:374px;text-align:center;color:#dbe7f3;font-size:13px;line-height:1.5}
.dots{position:absolute;left:0;right:0;top:424px;display:flex;justify-content:center;gap:8px}
.dots span{width:9px;height:9px;border-radius:50%;background:rgba(255,255,255,.55)}
.dots span:first-child{background:var(--white)}

.grid{position:absolute;left:0;top:440px;width:1200px;display:grid;grid-template-columns:repeat(4,300px);grid-template-rows:310px 310px}
.tile-photo{width:300px;height:310px}
.tile-text{padding:34px 30px;background:var(--white)}
.tile-text h2{font-size:22px;font-weight:800;text-transform:uppercase;color:#222;margin-bottom:12px}
.tile-text p{font-size:12px;line-height:1.6;color:var(--muted);margin-bottom:20px}
.tags{display:flex;gap:6px}
.tag{font-size:11px;font-weight:700;color:var(--white);padding:6px 12px}
.tag.talent{background:var(--lime)}
.tag.projects{background:var(--teal)}
.tag.jobs{background:var(--blue)}

.seams{position:absolute;left:0;top:1060px;width:1200px;height:410px;background:var(--teal);overflow:hidden}
.seams-photo{position:absolute;left:560px;top:0;width:640px;height:410px;background:linear-gradient(90deg,#6f8f4a,#8aa55a 45%,#5d7d3e 100%);clip-path:polygon(60px 0,640px 0,640px 410px,0 410px)}
.seams-copy{position:absolute;left:40px;top:120px;width:470px;color:var(--white)}
.seams-copy h2{font-size:26px;font-weight:800;text-transform:uppercase;margin-bottom:18px}
.seams-copy p{font-size:13px;line-height:1.65;color:#e8f7f4}

.search{position:absolute;left:0;top:1470px;width:1200px;height:260px;background:var(--blue);overflow:hidden}
.search-photo{position:absolute;right:0;top:0;width:480px;height:260px;background:linear-gradient(90deg,rgba(49,118,181,1),rgba(86,140,190,.9))}
.search h2{position:absolute;left:300px;top:60px;color:var(--white);font-size:22px;font-weight:800}
.search-fields{position:absolute;left:300px;top:104px;display:flex;gap:14px}
.field{width:286px;height:34px;background:var(--white);font-size:12px;color:var(--muted);padding:9px 12px}
.match-btn{position:absolute;left:480px;top:156px;background:var(--lime);color:var(--navy);font-size:11px;font-weight:700;padding:10px 26px;text-transform:uppercase}

.events{position:absolute;left:0;top:1730px;width:1200px;height:220px;background:var(--white)}
.calendar{position:absolute;left:280px;top:0;width:240px;border:1px solid var(--line);background:var(--white);box-shadow:0 2px 6px rgba(0,0,0,.12)}
.cal-head{background:#3c3f44;color:var(--white);font-size:12px;font-weight:700;text-align:center;padding:8px 0}
.calendar table{width:100%;border-collapse:collapse;font-size:10px;text-align:center;color:var(--ink)}
.calendar th{background:#f1f2f4;padding:4px 0;font-weight:600}
.calendar td{padding:5px 0;border:1px solid var(--line)}
.calendar td.today{background:var(--teal);color:var(--white)}
.events-copy{position:absolute;left:620px;top:30px;width:300px;font-size:12px;line-height:1.6;color:var(--muted)}
.start-btn{position:absolute;left:620px;top:100px;background:var(--lime);color:var(--navy);font-size:14px;font-weight:700;padding:10px 24px}

.map{position:absolute;left:0;top:1950px;width:1200px;height:310px;background:radial-gradient(circle at 30% 40%,#e9efdc 0%,rgba(233,239,220,0) 35%),radial-gradient(circle at 75% 70%,#dde6d2 0%,rgba(221,230,210,0) 40%),linear-gradient(135deg,#f1eee6,#e6e3da 50%,#efebe2)}
.contact-card{position:absolute;left:430px;top:2150px;width:170px;background:var(--white);padding:12px 14px;font-size:10px;line-height:1.5;color:var(--ink);box-shadow:0 2px 6px rgba(0,0,0,.2);display:flex;gap:8px}
.contact-card strong{display:block;font-size:11px}

.footer{position:absolute;left:0;top:2260px;width:1200px;height:192px;background:var(--footer);color:var(--white)}
.footer-nav{display:flex;justify-content:center;gap:34px;padding-top:20px;font-size:12px;font-weight:700;text-transform:uppercase}
.footer-select{width:140px;margin:18px auto 0;background:var(--white);color:var(--ink);font-size:10px;padding:5px 8px}
.socials{display:flex;justify-content:center;gap:10px;margin-top:18px}
.socials span{width:24px;height:24px;border-radius:50%}
.copyright{text-align:center;font-size:10px;color:#7d8288;margin-top:40px}
</style>
</head>
<body>

<header class="hero">
  <div class="hero-photo" role="img" aria-label="Photo of smiling professionals working together in an office, tinted blue and teal"></div>
  <div class="hero-band"></div>
  <div class="brand"><span class="brand-dot"></span>PathVerdantia</div>
  <nav class="menu-panel">
    <span class="menu-label">MENU</span>
    <ul>
      <li>Portfolios</li>
      <li>Projects</li>
      <li>Blog</li>
      <li>Resources</li>
      <li>Partners</li>
    </ul>
  </nav>
  <h1 class="hero-title">We are creating a collaborative career course,<br>with coaching and community exchange.</h1>
  <p class="hero-sub">Our aim is to offer a platform where talented candidates can show their expertise and find projects, partners, and develop their portfolios.</p>
  <div class="dots"><span></span><span></span><span></span><span></span></div>
</header>

<section class="grid">
  <div class="tile-photo" role="img" aria-label="Photo of fresh green vegetables and apples" style="background:linear-gradient(135deg,#7fae3a,#4f8a2c)"></div>
  <article class="tile-text">
    <h2>Food</h2>
    <p>Growers, analysts and planners share portfolios, case studies and field results here. Browse profiles by focus area, connect with partners and find short term projects that match your skills.</p>
    <div class="tags"><span class="tag talent">Talent</span><span class="tag projects">Projects</span><span class="tag jobs">Job Postings</span></div>
  </article>
  <div class="tile-photo" role="img" aria-label="Photo of water being poured into a glass" style="background:linear-gradient(160deg,#cfe3f2,#5f9fcf)"></div>
  <article class="tile-text">
    <h2>Water</h2>
    <p>Hydrologists, engineers and advocates present resumes, biographies and project work. Search by region or skill, meet collaborators and answer open calls from employers seeking water expertise.</p>
    <div class="tags"><span class="tag talent">Talent</span><span class="tag projects">Projects</span><span class="tag jobs">Job Postings</span></div>
  </article>
  <article class="tile-text">
    <h2>Energy</h2>
    <p>Renewable energy specialists show completed portfolios and case studies. Find consulting teams, internships and full time roles, or post a call for talent to build your next energy project.</p>
    <div class="tags"><span class="tag talent">Talent</span><span class="tag projects">Projects</span><span class="tag jobs">Job Postings</span></div>
  </article>
  <div class="tile-photo" role="img" aria-label="Photo of solar panels and wind turbines under a blue sky" style="background:linear-gradient(160deg,#9cc3e6,#3d6f9e)"></div>
  <article class="tile-text">
    <h2>Public Health</h2>
    <p>Health practitioners and researchers exhibit their work and connect across disciplines. Browse portfolios, discover project openings and match community needs with the right people and partners.</p>
    <div class="tags"><span class="tag talent">Talent</span><span class="tag projects">Projects</span><span class="tag jobs">Job Postings</span></div>
  </article>
  <div class="tile-photo" role="img" aria-label="Photo of a doctor in a white coat" style="background:linear-gradient(160deg,#e8eef3,#a9bccb)"></div>
</section>

<section class="seams">
  <div class="seams-photo" role="img" aria-label="Photo of a large group of young people outdoors under trees"></div>
  <div class="seams-copy">
    <h2>Steering Through Seams</h2>
    <p>A shared blog space where people mix it up across topic issues. Sustainability challenges are interdependent and often require partners across disciplines, so share articles, discuss ideas and build the teams that close the gap.</p>
  </div>
</section>

<section class="search">
  <div class="search-photo" role="img" aria-label="Photo of hands typing on a laptop keyboard"></div>
  <h2>SEARCH</h2>
  <div class="search-fields">
    <div class="field">Talent</div>
    <div class="field">Task opportunity</div>
  </div>
  <div class="match-btn">Match the community member</div>
</section>

<section class="events">
  <div class="calendar">
    <div class="cal-head">March 2017</div>
    <table>
      <tr><th>Su</th><th>Mo</th><th>Tu</th><th>We</th><th>Th</th><th>Fr</th><th>Sa</th></tr>
      <tr><td></td><td></td><td></td><td>1</td><td>2</td><td>3</td><td>4</td></tr>
      <tr><td>5</td><td>6</td><td>7</td><td>8</td><td>9</td><td>10</td><td>11</td></tr>
      <tr><td>12</td><td>13</td><td class="today">14</td><td>15</td><td>16</td><td>17</td><td>18</td></tr>
      <tr><td>19</td><td>20</td><td>21</td><td>22</td><td>23</td><td>24</td><td>25</td></tr>
      <tr><td>26</td><td>27</td><td>28</td><td>29</td><td>30</td><td>31</td><td></td></tr>
    </table>
  </div>
  <p class="events-copy">See our upcoming networking opportunities, issue presentations where potential partners can meet the next generation leaders, forums and webinars.</p>
  <div class="start-btn">Get Started</div>
</section>

<div class="map" role="img" aria-label="Street map of the city showing the office location"></div>
<div class="contact-card">
  <svg width="14" height="18" viewBox="0 0 14 18" aria-hidden="true"><path d="M7 0C3 0 0 3 0 7c0 5 7 11 7 11s7-6 7-11C14 3 11 0 7 0z" fill="#3176b5"/><circle cx="7" cy="7" r="2.5" fill="#fff"/></svg>
  <div><strong>Company Name</strong>Main Street 1200<br>Green Valley<br>Your Postal Code</div>
</div>

<footer class="footer">
  <nav class="footer-nav"><span>Home</span><span>About Us</span><span>Services</span><span>Blog</span><span>Contact Us</span></nav>
  <div class="footer-select">Select Month ▾</div>
  <div class="socials">
    <span style="background:#3b5a98"></span>
    <span style="background:#2fa5dc"></span>
    <span style="background:#d9473a"></span>
    <span style="background:#2f7bb5"></span>
    <span style="background:#c4302b"></span>
  </div>
  <p class="copyright">© 2024 PathVerdantia. All rights reserved.</p>
</footer>

</body>
</html>
```